Covid19 Poster for workplaces

Create a poster on how to protect yourself from Corona virus at work.
We are a Worklife Thrive company. We have just re-branded so we need to fit in with our brand. We like clean and fresh, slightly amusing is ok if it will draw attention but it's an important topic. A4 and A3 please.

Content:

Headline: Lower the risk of COVID 19 in the workplace.

BE WELL

Bring your own cup - don’t share cups and food.
Elbow tap instead of handshakes and kisses
Wash your hands often - with soap.
Elbow or tissues when you cough or sneeze then straight in the bin
Leave your face alone after touching shared surfaces
Leave your bugs at home if you’re feeling unwell.

Call health line if you have a cough, a high temperature and shortness of breath. 0800 472 9160

Based on recommendations from IPB and DCT

Target Market(s)

Employees - so anyone

Other font styles liked:
• Use the closest font to the brand documents

Requirements
Should not have
• Clip art

```html
<!DOCTYPE html>
<html lang="en">
<head>
<meta charset="utf-8">
<title>Wellbeing Matters at Work</title>
<link href="https://fonts.googleapis.com/css2?family=Archivo+Black&family=Figtree:wght@400;600&display=swap" rel="stylesheet">
<style>
  :root {
    --teal: #1aabb5;
    --ink: #141414;
    --white: #ffffff;
    --photo-dark: #1f2a33;
    --photo-warm: #6b5a4a;
  }
  * { margin: 0; padding: 0; box-sizing: border-box; }
  html, body { width: 848px; height: 1200px; overflow: hidden; background: var(--white); }
  .poster {
    position: relative;
    width: 848px;
    height: 1200px;
    background: var(--white);
    font-family: "Figtree", "Helvetica Neue", Arial, sans-serif;
    color: var(--ink);
    overflow: hidden;
  }
  .corner { position: absolute; top: 0; }
  .corner--left { left: 0; }
  .corner--right { right: 0; }
  .hero-photo {
    position: absolute;
    left: 243px;
    top: 44px;
    width: 362px;
    height: 194px;
    border-radius: 60px;
    background: linear-gradient(110deg, var(--photo-warm) 0%, var(--photo-dark) 45%, #3a4650 100%);
  }
  .title {
    position: absolute;
    left: 0; right: 0;
    top: 262px;
    text-align: center;
    font-family: "Archivo Black", "Arial Black", sans-serif;
    font-size: 37px;
    letter-spacing: 3px;
    color: var(--ink);
  }
  .headline {
    position: absolute;
    left: 0; right: 0;
    top: 334px;
    text-align: center;
    font-weight: 600;
    font-size: 31px;
    letter-spacing: -0.3px;
    color: var(--teal);
  }
  .checklist { list-style: none; position: absolute; left: 31px; top: 0; width: 790px; }
  .checklist__item {
    position: absolute;
    left: 0;
    width: 790px;
    display: flex;
    align-items: flex-start;
    font-size: 22px;
    line-height: 31px;
  }
  .tick { width: 36px; height: 30px; flex: none; margin-right: 13px; margin-top: -4px; }
  .band {
    position: absolute;
    left: 0; top: 1004px;
    width: 848px; height: 196px;
    background: var(--teal);
  }
  .brand {
    position: absolute;
    left: 270px; top: 1042px;
    display: flex;
    align-items: center;
    gap: 26px;
  }
  .brand__dot { width: 70px; height: 70px; border-radius: 50%; background: var(--white); }
  .brand__name {
    font-weight: 600;
    font-size: 42px;
    line-height: 40px;
    color: var(--white);
    letter-spacing: -0.5px;
  }
  .website {
    position: absolute;
    left: 0; right: 0;
    top: 1148px;
    text-align: center;
    font-size: 22px;
    color: var(--ink);
  }
</style>
</head>
<body>
<div class="poster">
  <svg class="corner corner--left" width="276" height="276" viewBox="0 0 276 276"><polygon points="0,0 275,0 0,275" fill="var(--teal)"/></svg>
  <svg class="corner corner--right" width="276" height="276" viewBox="0 0 276 276"><polygon points="0,0 276,0 276,275" fill="var(--teal)"/></svg>

  <div class="hero-photo" role="img" aria-label="Photo of smiling colleagues chatting at their desks in an office"></div>

  <h1 class="title">Wellbeing Matters at Work</h1>
  <h2 class="headline">Lower the risk of COVID 19 in the workplace</h2>

  <svg width="0" height="0" style="position:absolute">
    <defs>
      <symbol id="tick" viewBox="0 0 36 30">
        <path d="M1 17 L5 14 L12 21 C18 11 26 4 35 0 C27 6 19 15 13 29 Z" fill="var(--ink)"/>
      </symbol>
    </defs>
  </svg>

  <ul class="checklist">
    <li class="checklist__item" style="top:428px"><svg class="tick"><use href="#tick"/></svg>Bring your cup - don’t share cups and food</li>
    <li class="checklist__item" style="top:499px"><svg class="tick"><use href="#tick"/></svg>Elbow tap instead of handshakes and kisses</li>
    <li class="checklist__item" style="top:570px"><svg class="tick"><use href="#tick"/></svg>Wash your hands often - with soap</li>
    <li class="checklist__item" style="top:641px"><svg class="tick"><use href="#tick"/></svg>Elbow or tissues when you cough or sneeze then straight in the bin</li>
    <li class="checklist__item" style="top:713px"><svg class="tick"><use href="#tick"/></svg>Leave your face alone after touching shared surfaces</li>
    <li class="checklist__item" style="top:784px"><svg class="tick"><use href="#tick"/></svg>Leave your bugs at home if you’re feeling unwell</li>
    <li class="checklist__item" style="top:849px"><svg class="tick"><use href="#tick"/></svg><span>Call health line if you have a cough, high temperature or shortness<br>of breath at 0800 472 9160</span></li>
  </ul>

  <footer class="band">
  </footer>
  <div class="brand">
    <div class="brand__dot"></div>
    <div class="brand__name">Worklife<br>Thrive</div>
  </div>
  <div class="website">worklifethrive.co.nz</div>
</div>
</body>
</html>
```